Quiet Iron Hours - Cover for a book exploring On Quiet Strength and Open Hearts

The book explores what men in today's world think and feel, and what they want from society and the people in their lives. The idea is to put the focus on men and how they're dealing with a world in which patriarchy is rightly under scrutiny and women are finding and using their voice. How do men feel in the company of more empowered women? What do men want from the women in their lives (not talking about sex here)? Why are men more likely to take their own lives, not coping well with mental health issues?

Target Market(s)

Men and Women

Font styles to use
Other font styles liked:
• Clean and non-fussy font

Colors

Designer to choose colors to be used in the design.

Requirements
Must have
• A silhouette of a man or multiple men from diverse backgrounds and age groups
Nice to have
• The image must be bold and yet understated in its simplicity.
Should not have
• Nothing sexual or suggestive.

```html
<!DOCTYPE html>
<html lang="en">
<head>
<meta charset="utf-8">
<title>Quiet Iron Hours — Book Cover</title>
<link rel="stylesheet" href="https://fonts.googleapis.com/css2?family=Fira+Sans:wght@700;800&family=Fira+Sans+Condensed:wght@700&display=swap">
<style>
  :root {
    --sky-top: #0f98da;
    --sky-mid: #86cdee;
    --sky-glow: #ffffff;
    --ink: #2f2f30;
    --ground: #1f1f1f;
    --title-light: #ffffff;
    --page: #ffffff;
    --edge: #3a3a3a;
  }
  html, body {
    margin: 0;
    padding: 0;
    width: 1200px;
    height: 907px;
    overflow: hidden;
    background: var(--page);
  }
  .book-cover {
    position: absolute;
    left: 297px;
    top: 23px;
    width: 606px;
    height: 860px;
    overflow: hidden;
    box-sizing: border-box;
    border: 1px solid var(--edge);
    background:
      radial-gradient(ellipse 90% 40% at 50% 68%, var(--sky-glow) 0%, rgba(255,255,255,0.6) 45%, rgba(255,255,255,0) 100%),
      linear-gradient(to bottom, var(--sky-top) 0%, var(--sky-mid) 38%, #dff1fa 58%, var(--sky-glow) 70%);
  }
  .cover-title {
    position: absolute;
    right: 54px;
    top: 30px;
    margin: 0;
    font-family: "Fira Sans", sans-serif;
    font-weight: 800;
    text-align: right;
    line-height: 1;
  }
  .title-line { display: block; white-space: nowrap; }
  .title-top { color: var(--title-light); }
  .title-small { font-size: 54px; letter-spacing: -1px; margin-right: 8px; vertical-align: 6px; }
  .title-large { font-size: 116px; letter-spacing: -2px; }
  .title-bottom {
    color: var(--ink);
    font-size: 118px;
    letter-spacing: -2px;
    margin-top: -14px;
  }
  .cover-subtitle {
    position: absolute;
    left: 289px;
    top: 398px;
    margin: 0;
    font-family: "Fira Sans Condensed", sans-serif;
    font-weight: 700;
    font-size: 31px;
    line-height: 45px;
    color: var(--ink);
    text-transform: uppercase;
    letter-spacing: 0.2px;
    white-space: nowrap;
  }
  .figure-silhouette {
    position: absolute;
    left: 42px;
    top: 200px;
    width: 172px;
    height: 520px;
    border-radius: 60px 60px 10px 10px;
    background: linear-gradient(to bottom, #2a2a2a 0%, var(--ground) 100%);
  }
  .ground-silhouette {
    position: absolute;
    left: 0;
    bottom: 0;
    width: 100%;
    height: 270px;
  }
</style>
</head>
<body>
  <main class="book-cover">
    <div class="figure-silhouette" role="img" aria-label="Black silhouette of a hooded man standing with his back turned, looking out over the horizon"></div>
    <svg class="ground-silhouette" viewBox="0 0 606 270" preserveAspectRatio="none" role="img" aria-label="Dark silhouette of rocky shoreline in the foreground">
      <path d="M0 50 L40 42 L120 58 L220 72 L320 66 L430 72 L510 36 L560 18 L606 4 L606 270 L0 270 Z" fill="var(--ground)"/>
    </svg>
    <h1 class="cover-title">
      <span class="title-line title-top"><span class="title-small">Quiet</span><span class="title-large">Iron</span></span>
      <span class="title-line title-bottom">Hours</span>
    </h1>
    <p class="cover-subtitle">On quiet strength<br>and open hearts</p>
  </main>
</body>
</html>
```